Farrin Lodsway Christmas Seasons Greetings

we would require a contemporarely designed and colorful christmas greetings card in landscape format A5, featuring a cup of coffee and happy faces - preferable asian and caucasian refer to attached pictures. inside a light paper insert with wording 'wishing you a warm Christmas and Happy New Year... from all of us @ F.L Professional Thailand'. Back of Card the following text: Farrin Lodsway Professional | Velmuta (Thailand) Limited | Pinegate Plaza A, 34th Floor | 57 Sonthiwarin Road | Kwaeng Huay Kwang | Khet Huay Kwang | Bangkok | 10485

```html
<!DOCTYPE html>
<html lang="en">
<head>
<meta charset="utf-8">
<title>Farrin Lodsway Professional – Christmas Greetings Card</title>
<link rel="stylesheet" href="https://fonts.googleapis.com/css2?family=Ubuntu:wght@400;500;700&family=Lobster&display=swap">
<style>
  :root {
    --page: #ffffff;
    --label: #9a3a3c;
    --card-red-dark: #9e2b33;
    --card-red: #c8403f;
    --card-red-light: #dd5a4e;
    --gold: #e6b24a;
    --gold-bright: #f4d23a;
    --script-ink: #3a4566;
    --white: #ffffff;
    --back-orange: #f0a54c;
    --back-ink: #7a3a30;
    --back-ink-soft: #8a4a3c;
  }
  * { margin: 0; padding: 0; box-sizing: border-box; }
  html, body { width: 889px; height: 1200px; overflow: hidden; background: var(--page); }
  body { font-family: "Ubuntu", Arial, sans-serif; }
  .sheet { position: relative; width: 889px; height: 1200px; }

  .side-label {
    position: absolute; left: 0; width: 889px; text-align: center;
    font-weight: 700; font-size: 29px; color: var(--label);
    text-shadow: 1px 1px 2px rgba(0,0,0,.25);
  }
  .side-label--front { top: 40px; }
  .side-label--back { top: 593px; }

  .card { position: absolute; left: 132px; width: 636px; height: 449px; overflow: hidden; }
  .card--front {
    top: 96px;
    background: linear-gradient(115deg, var(--card-red-dark) 0%, var(--card-red) 45%, var(--card-red-light) 100%);
  }
  .card--back { top: 647px; background: var(--back-orange); }

  .greeting-lead {
    position: absolute; left: 41px; top: 12px;
    font-size: 20px; color: var(--gold);
  }
  .greeting-script {
    position: absolute; left: 0; width: 516px; text-align: center;
    font-family: "Lobster", cursive; color: var(--script-ink);
    text-shadow: 1px 1px 0 var(--gold), -1px -1px 0 rgba(244,210,58,.6), 2px 3px 4px rgba(0,0,0,.35);
    line-height: 1;
  }
  .greeting-script--christmas { top: 62px; font-size: 48px; width: 490px; }
  .greeting-and {
    position: absolute; left: 0; width: 490px; text-align: center; top: 114px;
    font-size: 20px; color: var(--gold);
  }
  .greeting-script--newyear { top: 148px; font-size: 52px; }

  .art { position: absolute; }
  .art--swoosh {
    left: 140px; top: 250px; width: 496px; height: 112px;
  }
  .art--tree {
    left: 443px; top: 78px; width: 173px; height: 272px;
    background: radial-gradient(ellipse at 50% 55%, rgba(246,206,120,.85) 0%, rgba(238,150,110,.5) 45%, rgba(200,64,63,0) 72%);
  }
  .art--couple {
    left: 0; top: 206px; width: 416px; height: 243px;
    background: linear-gradient(160deg, #6c6f78 0%, #8b97ad 45%, #4a6c9e 75%, #c9c9c4 100%);
  }

  .signoff {
    position: absolute; left: 429px; font-size: 16px; line-height: 1;
  }
  .signoff--from { top: 396px; color: var(--white); }
  .signoff--company { top: 420px; color: var(--gold-bright); }

  .back-address {
    position: absolute; left: 0; width: 636px; text-align: center;
    text-shadow: 1px 1px 1px rgba(0,0,0,.2);
  }
  .back-address__company { top: 326px; font-size: 18px; font-weight: 700; color: var(--back-ink); }
  .back-address__line { font-size: 15.5px; color: var(--back-ink-soft); }
  .back-address__line--one { top: 362px; }
  .back-address__line--two { top: 385px; }
</style>
</head>
<body>
<main class="sheet">
  <h2 class="side-label side-label--front">Front</h2>

  <section class="card card--front" aria-label="Card front">
    <svg class="art art--swoosh" role="img" aria-label="Flowing golden light swoosh" viewBox="0 0 496 112" preserveAspectRatio="none">
      <defs>
        <linearGradient id="swooshGlow" x1="0" y1="0" x2="1" y2="0">
          <stop offset="0" stop-color="#f6c24a" stop-opacity="0"/>
          <stop offset="0.35" stop-color="#f6a83a" stop-opacity="0.85"/>
          <stop offset="1" stop-color="#f3c84a" stop-opacity="0.6"/>
        </linearGradient>
      </defs>
      <path d="M0 40 C120 20 220 110 340 80 C420 60 470 50 496 56 L496 84 C450 84 400 100 330 104 C210 112 110 60 0 60 Z" fill="url(#swooshGlow)"/>
    </svg>

    <div class="art art--tree" role="img" aria-label="Sparkling Christmas tree of gold ribbons and stars"></div>

    <div class="art art--couple" role="img" aria-label="Photo of a smiling couple sitting together holding coffee cups"></div>

    <p class="greeting-lead">wishing you a warm</p>
    <p class="greeting-script greeting-script--christmas">Christmas</p>
    <p class="greeting-and">And</p>
    <p class="greeting-script greeting-script--newyear">Happy New Year</p>

    <p class="signoff signoff--from">from all of us @</p>
    <p class="signoff signoff--company">F.L Professional Thailand</p>
  </section>

  <h2 class="side-label side-label--back">Back</h2>

  <section class="card card--back" aria-label="Card back">
    <p class="back-address back-address__company">Farrin Lodsway Professional | Velmuta (Thailand) Limited |</p>
    <p class="back-address back-address__line back-address__line--one">Pinegate Plaza A, 34th Floor | 57 Sonthiwarin Road |</p>
    <p class="back-address back-address__line back-address__line--two">Kwaeng Huay Kwang | Khet Huay Kwang | Bangkok | 10485</p>
  </section>
</main>
</body>
</html>
```